Morrowlane Systems - Company Overview Brochure

We would like a single page A4 Brochure to give to new potential customers to provide a quick overview of our company. This will be used in presales meetings.

We have included the content we would like on the brochure under "Morrowlane Systems Marketing Brochure.docx".

We have included two other designs "servicetermsheet v4.pdf and Morrowlane Public Cloud Plans.pdf" which shows similar marketing brochures we have. We would like these designs to have the same Morrowlane Blue and "Specialised Technology Consultancy firm" theme.

Target Market(s)

Technology Sector

Industry/Entity Type

Information Technology

Colors
0054AA
0677BA
7BADD7
CADEEF
E8F1F8

Requirements
Must have
• "Innovative Tech Company Theme".

```html
<!DOCTYPE html>
<html lang="en">
<head>
<meta charset="utf-8">
<title>Morrowlane Systems – Specialised Consulting</title>
<link href="https://fonts.googleapis.com/css2?family=Saira:wght@700&family=Exo+2:wght@600;700&family=Mulish:ital,wght@0,500;1,500&display=swap" rel="stylesheet">
<style>
  :root {
    --page-bg: #d6d6d6;
    --deep-indigo: #2b2f9c;
    --royal-blue: #2a4fb0;
    --bright-blue: #0a80d2;
    --brand-blue: #0054AA;
    --accent-blue: #5db3ec;
    --frame-cyan: #3fb6e6;
    --label-grey: #d5d7dd;
    --label-text: #1f2c7a;
    --white: #ffffff;
  }
  * { margin: 0; padding: 0; box-sizing: border-box; }
  html, body { width: 1200px; height: 2246px; overflow: hidden; background: var(--page-bg); }
  .brochure {
    position: absolute; left: 70px; top: 373px; width: 1060px; height: 1500px;
    background:
      radial-gradient(ellipse 70% 45% at 95% 5%, var(--bright-blue) 0%, rgba(10,128,210,0) 70%),
      linear-gradient(160deg, var(--royal-blue) 0%, #2a44ad 35%, var(--deep-indigo) 75%, #2b2b95 100%);
    color: var(--white); font-family: 'Mulish', sans-serif; overflow: hidden;
  }
  .headline {
    position: absolute; left: 99px; top: 122px;
    font-family: 'Saira', sans-serif; font-weight: 700; font-size: 68px; line-height: 68px; letter-spacing: -0.5px;
  }
  .brand-panel {
    position: absolute; left: 478px; top: 113px; width: 582px; height: 149px;
    background: var(--white); clip-path: polygon(0 0, 100% 0, 100% 100%, 62px 100%);
    display: flex; align-items: center; justify-content: center; gap: 16px; padding-left: 60px;
  }
  .brand-mark { width: 30px; height: 30px; background: var(--brand-blue); }
  .brand-name {
    font-family: 'Exo 2', sans-serif; font-weight: 700; font-size: 34px; color: var(--brand-blue); letter-spacing: 1px;
  }
  .intro { position: absolute; left: 99px; top: 308px; width: 660px; font-size: 17.5px; line-height: 22px; }
  .section-label {
    position: absolute; left: 0; height: 38px; padding-left: 99px; padding-right: 14px;
    background: linear-gradient(90deg, #9a9ea8 0%, var(--label-grey) 30%, #eceef2 100%);
    font-family: 'Exo 2', sans-serif; font-weight: 700; font-size: 21px; line-height: 38px; color: var(--label-text);
  }
  .label-it { top: 437px; width: 229px; }
  .label-esc { top: 685px; width: 512px; }
  .service-box {
    position: absolute; left: 99px; width: 862px; height: 179px;
    border: 2px solid var(--frame-cyan); border-radius: 10px;
    display: grid; grid-template-columns: repeat(4, 1fr); padding: 0 60px 0 70px;
  }
  .box-it { top: 475px; }
  .box-esc { top: 722px; }
  .service {
    display: flex; flex-direction: column; align-items: center; justify-content: center; gap: 10px;
    text-align: center; font-size: 15px; line-height: 15px; position: relative;
  }
  .service + .service::before {
    content: ""; position: absolute; left: 0; top: 22px; bottom: 22px; width: 1px; background: rgba(255,255,255,0.55);
  }
  .service svg { width: 86px; height: 86px; fill: var(--white); }
  .heading {
    position: absolute; left: 99px; font-family: 'Exo 2', sans-serif; font-weight: 700; font-size: 26px; color: var(--accent-blue);
  }
  .h-commit { top: 930px; }
  .h-policy { top: 1120px; }
  .body-copy { position: absolute; left: 99px; width: 862px; font-size: 13.6px; line-height: 17px; }
  .copy-commit { top: 968px; }
  .copy-commit p + p { margin-top: 17px; }
  .copy-commit p.tight { margin-top: 0; }
  .policy { top: 1160px; }
  .policy .sub { font-style: italic; color: var(--accent-blue); margin-bottom: 9px; }
  .policy p + .sub { margin-top: 18px; }
  .terms { position: absolute; left: 99px; top: 1374px; font-size: 13.6px; line-height: 17px; font-style: italic; }
</style>
</head>
<body>
<main class="brochure">
  <h1 class="headline">Specialised<br>Consulting</h1>
  <div class="brand-panel">
    <span class="brand-mark"></span>
    <span class="brand-name">MORROWLANE SYSTEMS</span>
  </div>
  <p class="intro">Morrowlane Systems is a Technology Consulting Company based in Perth, Western Australia, which offers customers tailored technical solutions for a range of products.</p>

  <div class="section-label label-it">IT Services</div>
  <section class="service-box box-it">
    <div class="service">
      <svg viewBox="0 0 64 64"><circle cx="32" cy="18" r="9"/><path d="M16 46c0-9 7-15 16-15s16 6 16 15z"/><rect x="10" y="48" width="44" height="5" rx="2"/><rect x="44" y="14" width="14" height="12" rx="2"/><circle cx="10" cy="18" r="5"/></svg>
      <span>Project<br>Integration</span>
    </div>
    <div class="service">
      <svg viewBox="0 0 64 64"><circle cx="42" cy="20" r="11"/><path d="M37 20l4 4 7-8" stroke="#2a44ad" stroke-width="3" fill="none"/><path d="M6 44l12-6h14l10-6 4 4-12 12H14z"/><path d="M12 10l2 4 4 .5-3 3 .7 4-3.7-2-3.7 2 .7-4-3-3 4-.5z"/></svg>
      <span>Managed<br>Services</span>
    </div>
    <div class="service">
      <svg viewBox="0 0 64 64"><path d="M32 6l20 8v14c0 14-9 24-20 30-11-6-20-16-20-30V14z"/><rect x="24" y="28" width="16" height="13" rx="2" fill="#2a44ad"/><path d="M27 28v-4a5 5 0 0 1 10 0v4" stroke="#2a44ad" stroke-width="3" fill="none"/></svg>
      <span>Enterprise<br>Security</span>
    </div>
    <div class="service">
      <svg viewBox="0 0 64 64"><circle cx="32" cy="18" r="10"/><path d="M14 44c0-10 8-16 18-16s18 6 18 16z"/><rect x="20" y="38" width="24" height="14" rx="2" fill="#2a44ad" stroke="#fff" stroke-width="2"/><path d="M4 30h8M52 30h8M4 40h8M52 40h8" stroke="#fff" stroke-width="2"/></svg>
      <span>Software<br>Development</span>
    </div>
  </section>

  <div class="section-label label-esc">Electronic Security &amp; Communications</div>
  <section class="service-box box-esc">
    <div class="service">
      <svg viewBox="0 0 64 64"><path d="M14 16l40 14-5 10-40-14z"/><rect x="8" y="38" width="6" height="18"/><path d="M14 46l12-4 2 5-14 4z"/></svg>
      <span>CCTV</span>
    </div>
    <div class="service">
      <svg viewBox="0 0 64 64"><path d="M32 6l22 8v16c0 14-10 24-22 30C20 54 10 44 10 30V14z"/><path d="M35 18l-10 16h7l-3 12 10-16h-7z" fill="#2a44ad"/></svg>
      <span>Integrated Electronic<br>Security</span>
    </div>
    <div class="service">
      <svg viewBox="0 0 64 64"><rect x="22" y="30" width="20" height="22" rx="4"/><path d="M26 30V12M32 30V8M38 30V12M22 34l-12-14M42 34l12-14" stroke="#fff" stroke-width="3" fill="none"/><circle cx="26" cy="10" r="3"/><circle cx="32" cy="6" r="3"/><circle cx="38" cy="10" r="3"/></svg>
      <span>Structured Cabling<br>&amp; Fibre Optics</span>
    </div>
    <div class="service">
      <svg viewBox="0 0 64 64" fill="none" stroke="#fff" stroke-width="4"><circle cx="32" cy="28" r="4" fill="#fff"/><path d="M32 32v22"/><path d="M22 18a14 14 0 0 0 0 20M42 18a14 14 0 0 1 0 20M14 10a26 26 0 0 0 0 36M50 10a26 26 0 0 1 0 36"/></svg>
      <span>Wireless<br>Communications</span>
    </div>
  </section>

  <h2 class="heading h-commit">Our Commitment</h2>
  <div class="body-copy copy-commit">
    <p>Our commitment to you is to do things right the first time while being fair but cost-effective. If you're looking for the cheapest consultants, Morrowlane may not be the right fit for you.</p>
    <p class="tight">We are a specialised consultancy firm that offers tailored solutions to government and the enterprise sector with some of Perth's best consultants.</p>
    <p>In areas such as cybersecurity and business continuity, it pays to get it done correctly the first time in alignment with vendor best practices. There are many ways of doing things in the technology field, and only after understanding all methods of achieving an outcome can you recommend the best solution in alignment with best practices.</p>
  </div>

  <h2 class="heading h-policy">Our Policy</h2>
  <div class="body-copy policy">
    <p class="sub">Be Fair</p>
    <p>“At Morrowlane we believe that both parties benefit when pricing is fair. If margins are too low, we may sacrifice service quality, and this ultimately harms our brand. If margins are too high, our customers have an incentive to seek alternative providers, and this compromises our growth and damages client relationships.”</p>
    <p class="sub">Be Cost-Effective</p>
    <p>“At Morrowlane we believe that it is possible to deliver both high quality at a fair cost, by providing services that are intelligent and efficient.”</p>
  </div>

  <p class="terms">All goods and services provided by Morrowlane are provided in accordance with our Standard Terms<br>and Conditions available at https://www.morrowlanesystems.com.au/t&amp;c</p>
</main>
</body>
</html>
```